Christmas Banner for frontpage of website

New online scarf store just opened needs a Christmas Banner stating Free Delivery (UK only). Also if it could incorporate guaranteed Christmas delivery if ordered before 18th (might be too wordy though?) I would really like it to bring some colour to the page. The page is currently black and white with a pink accent and is very simple which is why I would like something modern and elegant, simple but with some colour. It is a shopify store I understand the banner size should be 950px by 290px the website is www.velmorrow.co.uk

Target Market(s)

Ladies

Industry/Entity Type

Store

Requirements
Should not have
• Not to look tacky.

```html
<!DOCTYPE html>
<html lang="en">
<head>
<meta charset="utf-8">
<title>Velmorrow Christmas Banner</title>
<link rel="stylesheet" href="https://fonts.googleapis.com/css2?family=Tinos:ital,wght@0,400;1,400&family=Great+Vibes&display=swap">
<style>
  :root {
    --frame: #7b1c6e;
    --paper: #f4ddd2;
    --ink: #1a1a1a;
    --bullet: #8a1f86;
    --url-top: #8a4220;
    --url-bottom: #4a1a08;
    --festive-red: #b0121a;
    --festive-deep: #6e0a0e;
    --festive-gold: #e0a530;
    --festive-light: #fbf3ea;
    --script: #0fa9b8;
    --scarf-pink: #f03cc2;
    --skin: #f3d9cf;
  }
  * { margin: 0; padding: 0; box-sizing: border-box; }
  html, body {
    width: 1200px; height: 366px; overflow: hidden;
    background: #ffffff;
  }
  .banner {
    position: relative;
    width: 1200px; height: 366px;
    background: var(--paper);
    border: 3px solid var(--frame);
    overflow: hidden;
    font-family: "Tinos", "Times New Roman", serif;
    color: var(--ink);
  }
  .festive-panel {
    position: absolute; top: 0; left: 0;
    width: 101px; height: 100%;
    background: linear-gradient(90deg, var(--festive-deep), var(--festive-red) 45%, var(--festive-gold) 120%);
  }
  .festive-column {
    position: absolute; top: 0; left: 101px;
    width: 105px; height: 100%;
    background: linear-gradient(180deg, var(--festive-light) 0%, #f1e4c8 30%, #dfe8d5 55%, #f7dede 85%, var(--festive-light) 100%);
    border-right: 1px solid #e6cfc4;
  }
  .greeting {
    position: absolute;
    left: -55px; top: 138px;
    width: 420px;
    font-family: "Great Vibes", cursive;
    font-size: 66px;
    line-height: 80px;
    color: var(--script);
    -webkit-text-stroke: 1.4px #0a1a1c;
    transform: rotate(-50deg);
    transform-origin: center;
    white-space: nowrap;
    text-align: center;
  }
  .portrait {
    position: absolute; top: 0; right: 0;
    width: 196px; height: 100%;
    background: linear-gradient(200deg, var(--skin) 0%, var(--skin) 45%, #f7a3dc 70%, var(--scarf-pink) 100%);
  }
  .headline {
    position: absolute;
    left: 509px; top: 20px;
    font-size: 44px;
    line-height: 50px;
    font-weight: 400;
    letter-spacing: 0.6px;
    white-space: nowrap;
  }
  .perks {
    position: absolute;
    left: 258px; top: 111px;
    list-style: none;
    font-size: 30px;
    line-height: 35px;
    letter-spacing: 0.8px;
    white-space: nowrap;
  }
  .perks li { position: relative; padding-left: 26px; }
  .perks li::before {
    content: "";
    position: absolute; left: 2px; top: 15px;
    width: 11px; height: 11px; border-radius: 50%;
    background: var(--bullet);
  }
  .tagline {
    position: absolute;
    right: 217px; top: 214px;
    font-size: 24px;
    white-space: nowrap;
  }
  .web-address {
    position: absolute;
    left: 258px; top: 250px;
    font-size: 70px;
    line-height: 80px;
    letter-spacing: 1px;
    white-space: nowrap;
    color: var(--url-bottom);
    background: linear-gradient(180deg, var(--url-top), var(--url-bottom));
    -webkit-background-clip: text;
    background-clip: text;
    -webkit-text-fill-color: transparent;
    filter: drop-shadow(3px 3px 2px rgba(90, 40, 20, 0.45));
  }
</style>
</head>
<body>
  <div class="banner">
    <div class="festive-panel" role="img" aria-label="Red panel with a golden Christmas tree ornament"></div>
    <div class="festive-column" role="img" aria-label="Christmas illustrations: golden bells with a red bow, a decorated Christmas tree and wrapped red gifts"></div>

    <div class="portrait" role="img" aria-label="Illustration of a woman wearing a bright pink spotted scarf"></div>

    <div class="greeting">Merry Christmas</div>

    <h1 class="headline">Free Delivery (UK only)</h1>
    <ul class="perks">
      <li>Guaranteed Christmas delivery if ordered before 18th.</li>
      <li>Funky, thicker and thin Scarves.</li>
    </ul>
    <p class="tagline">“Wrap up in style.”</p>
    <p class="web-address">www.velmorrow.co.uk</p>
  </div>
</body>
</html>
```